Waste Oil Filter collection & disposal

Basically I need a 1 page website for the business called Brenmoor Waste Solutions.
We are a environmental service provider and we collect and dispose of waste oil filters to protect the environment from hazardous waste oil products.

This is the link to our current website: www.brenmoorwaste.co.nz

we want it to look fresh and better than our current website. we may potentially look at getting a new logo designed and are open to ideas/designs if you have any.

Industry/Entity Type

Business

Logo Text

Brenmoor Waste Solutions

Number of Pages Required

1 page

Requirements
Must have
• same colours as current website.
• description of what service we provide please refer to leaflet attached

```html
<!DOCTYPE html>
<html lang="en">
<head>
<meta charset="utf-8">
<title>Brenmoor Waste Solutions – Oil Filter Collection &amp; Disposal</title>
<link href="https://fonts.googleapis.com/css2?family=Montserrat:wght@400;500;600;700&display=swap" rel="stylesheet">
<style>
:root{
  --green:#6cbd45;
  --blue:#2b4596;
  --blue-dark:#243c86;
  --ink:#2f2f2f;
  --grey:#8a8a8a;
  --dark:#262626;
  --white:#ffffff;
}
*{margin:0;padding:0;box-sizing:border-box}
html,body{width:1200px;height:3243px;overflow:hidden}
body{position:relative;font-family:"Montserrat",Arial,sans-serif;color:var(--ink);background:var(--white)}
.abs{position:absolute}
.center{left:0;width:1200px;text-align:center}

/* hero */
.hero{top:0;left:0;width:1200px;height:497px;background:radial-gradient(ellipse at 60% 45%,#5a5d60 0%,#34373a 45%,#1c1d1f 100%)}
.brand{top:22px;left:78px;display:flex;align-items:center;gap:12px}
.brand-dot{width:52px;height:52px;border-radius:50%;border:3px solid var(--green)}
.brand-name{font-size:16px;font-weight:700;color:var(--green);text-transform:uppercase;line-height:1.2}
.brand-tag{font-size:11px;font-weight:500;color:var(--white)}
.nav{top:40px;left:530px;display:flex;gap:34px;font-size:12.5px;font-weight:600;color:var(--white)}
.nav .active{border-bottom:2px solid var(--white);padding-bottom:3px}
.nav-phone{top:38px;left:994px;font-size:16px;font-weight:600;color:var(--green);display:flex;align-items:center;gap:6px}
.hero-title{top:246px;font-size:35px;font-weight:600;color:var(--white)}
.hero-sub{top:290px;font-size:24px;font-weight:600;color:var(--white)}
.hero-chevron{top:444px;left:592px}
.quote-band{top:497px;left:0;width:1200px;height:78px;background:var(--green);color:#1f3a10;font-size:12.5px}
.quote-band .text{position:absolute;left:156px;top:30px}
.quote-band .cite{position:absolute;right:156px;top:30px;font-weight:600}

/* about */
.about-label{top:668px;left:156px;font-size:16px;font-weight:600;color:var(--green)}
.about-head{top:712px;left:156px;width:540px;font-size:23px;line-height:1.3;color:var(--ink)}
.about-photo{top:834px;left:156px;width:432px;height:199px;background:linear-gradient(135deg,#6f7a74,#2f7a55 55%,#a8a9a4)}
.about-text{top:712px;left:763px;width:290px;font-size:13.5px;line-height:1.62;color:var(--grey)}
.btn-green{top:873px;left:763px;width:128px;height:31px;background:var(--green);color:var(--white);font-size:12px;font-weight:600;text-align:center;line-height:31px}
.bin-shape{top:972px;left:962px;width:82px;height:141px;background:linear-gradient(#e4e4e4,#d8d8d8);border-radius:8px 8px 0 0}

/* pricing */
.pricing{top:1113px;left:0;width:1200px;height:487px;background:var(--blue)}
.sec-title-light{font-size:24px;font-weight:500;color:var(--white)}
.price-item{width:300px;text-align:center;color:var(--white)}
.price-ring{width:130px;height:130px;border-radius:50%;border:2px solid rgba(255,255,255,.35);margin:0 auto;display:flex;align-items:center;justify-content:center}
.price-ring.filled{background:var(--green);border-color:var(--green)}
.price-name{margin-top:34px;font-size:16px}
.price-name.bold{font-weight:700}
.price-amount{font-size:28px;margin-top:4px}
.btn-outline{top:1490px;left:519px;width:160px;height:32px;border:1.5px solid var(--green);color:var(--green);font-size:12px;font-weight:600;text-align:center;line-height:29px}

/* process */
.sec-title-blue{font-size:24px;font-weight:500;color:var(--blue)}
.process-sub{top:1713px;font-size:11.5px;color:var(--grey)}
.step{top:1780px;width:200px;text-align:center}
.step-label{margin-top:10px;font-size:11.5px;font-weight:600;color:var(--ink);line-height:1.5}
.step-label.current{color:var(--blue)}
.step-divider{top:1773px;width:1px;height:130px;background:#dedede}

/* oil */
.oil{top:1983px;left:0;width:1200px;height:237px;background:radial-gradient(ellipse at 70% 30%,#4a4a4a,#262626 60%,#1a1a1a)}
.oil-text{top:2101px;font-size:16px;font-weight:600;color:var(--white);line-height:1.5}
.oil-text em{font-style:normal;color:var(--green)}

/* gallery */
.gallery-img{top:2359px;width:281px;height:201px}
.g1{left:156px;background:linear-gradient(160deg,#d9dedb,#4a8f6a 60%,#7c8076)}
.g2{left:460px;background:linear-gradient(160deg,#5b5d5f,#2e3336 60%,#1c3a4a)}
.g3{left:763px;background:linear-gradient(160deg,#c7d4d2,#2f8a80 55%,#3d4a4e)}
.g2-overlay{top:2425px;left:460px;width:281px;text-align:center;color:var(--white);font-size:11.5px;font-weight:600}
.g2-badge{width:44px;height:44px;border-radius:50%;background:var(--green);margin:0 auto 12px;display:flex;align-items:center;justify-content:center}
.g-arrow{top:2447px;width:26px;height:26px;border-radius:50%;border:1.5px solid #b5b5b5;display:flex;align-items:center;justify-content:center}

/* contact */
.contact{top:2638px;left:0;width:1200px;height:605px;background:var(--blue)}
.field{background:var(--white);font-size:11px;color:#9a9a9a;padding:10px 14px}
.send{top:2986px;left:895px;width:48px;height:48px;border-radius:50%;background:var(--green);display:flex;align-items:center;justify-content:center}
.footer-addr{top:3019px;font-size:12px;color:var(--white)}
.footer-call{top:3054px;font-size:16px;font-weight:600;color:var(--green)}
.footer-call span{color:var(--white)}
.socials{top:3099px;left:533px;display:flex;gap:13px}
.social{width:24px;height:24px;border-radius:50%;background:rgba(255,255,255,.3)}
.social.on{background:var(--green)}
.copyright{top:3151px;font-size:11px;color:var(--white)}
</style>
</head>
<body>

<!-- hero -->
<div class="abs hero" role="img" aria-label="Pile of used oil filters"></div>
<div class="abs brand">
  <div class="brand-dot"></div>
  <div>
    <div class="brand-name">Brenmoor Waste Solutions</div>
    <div class="brand-tag">Our Aim is to Keep NZ Green</div>
  </div>
</div>
<nav class="abs nav">
  <span class="active">About Us</span><span>Pricing</span><span>The Process</span><span>Gallery</span><span>Contact Us</span>
</nav>
<div class="abs nav-phone">
  <svg width="14" height="14" viewBox="0 0 24 24"><path fill="none" stroke="#6cbd45" stroke-width="2.4" d="M5 3h4l2 5-2.5 1.5a11 11 0 0 0 6 6L16 13l5 2v4a2 2 0 0 1-2 2A16 16 0 0 1 3 5a2 2 0 0 1 2-2z"/></svg>
  06 555 0142
</div>
<h1 class="abs center hero-title">Oil Filter Collection &amp; Disposal Service</h1>
<p class="abs center hero-sub">Lower North Island on a Monthly Cycle.</p>
<svg class="abs hero-chevron" width="16" height="10" viewBox="0 0 16 10"><path d="M2 2l6 6 6-6" fill="none" stroke="#fff" stroke-width="2"/></svg>
<div class="abs quote-band">
  <span class="text">Each used oil filter has on average, more than quarter of a litre of used motor oil.</span>
  <span class="cite">– FilterCycle</span>
</div>

<!-- about -->
<p class="abs about-label">Brenmoor Waste Solutions Ltd</p>
<h2 class="abs about-head" style="font-weight:400">Specialize in the collection &amp; disposal of oil / fuel filters, servicing the lower north island on a monthly cycle.</h2>
<div class="abs about-photo" role="img" aria-label="Green filter processing machine in the plant"></div>
<p class="abs about-text">We offer a cost effective environmentally friendly system for the collection and disposal of waste oil filters helping minimise contamination of landfills keeping your industry compliant.</p>
<div class="abs btn-green">Contact Us</div>
<div class="abs bin-shape" role="img" aria-label="Faint wheelie bin illustration"></div>

<!-- pricing -->
<section class="abs pricing"></section>
<h2 class="abs center sec-title-light" style="top:1184px">Pricing Packages</h2>
<div class="abs price-item" style="top:1245px;left:146px">
  <div class="price-ring"><svg width="56" height="40" viewBox="0 0 56 40"><rect x="2" y="8" width="32" height="22" fill="#6cbd45"/><path d="M34 14h12l8 8v8H34z" fill="#6cbd45"/><circle cx="14" cy="33" r="5" fill="#fff"/><circle cx="44" cy="33" r="5" fill="#fff"/></svg></div>
  <div class="price-name">Monthly Bin Collection</div>
  <div class="price-amount">$65.00</div>
</div>
<div class="abs price-item" style="top:1245px;left:449px">
  <div class="price-ring filled"><svg width="40" height="46" viewBox="0 0 40 46"><rect x="6" y="10" width="28" height="34" rx="2" fill="#fff"/><rect x="2" y="4" width="36" height="6" fill="#fff"/></svg></div>
  <div class="price-name bold">Additional Bins</div>
  <div class="price-amount">$35.00</div>
</div>
<div class="abs price-item" style="top:1245px;left:754px">
  <div class="price-ring"><svg width="40" height="40" viewBox="0 0 40 40"><circle cx="16" cy="12" r="8" fill="#6cbd45"/><path d="M2 36c0-10 6-15 14-15s10 3 12 6l-6 9z" fill="#6cbd45"/><path d="M26 36l10-12 3 3-10 12h-3z" fill="#6cbd45"/></svg></div>
  <div class="price-name">Account Set Up Fee</div>
  <div class="price-amount">$85.00</div>
</div>
<div class="abs btn-outline">Ready to Help You</div>

<!-- process -->
<h2 class="abs center sec-title-blue" style="top:1673px">The Process</h2>
<p class="abs center process-sub">Filters are collected and transported back to the processing plant.</p>
<div class="abs step" style="left:84px"><svg width="56" height="56" viewBox="0 0 56 56"><circle cx="28" cy="28" r="22" fill="none" stroke="#6cbd45" stroke-width="2.5" stroke-dasharray="30 5"/><text x="28" y="33" text-anchor="middle" font-family="Montserrat,sans-serif" font-size="14" fill="#2f2f2f">1</text></svg><div class="step-label">Drained Oil<br>Filter</div></div>
<div class="abs step-divider" style="left:288px"></div>
<div class="abs step" style="left:289px"><svg width="56" height="56" viewBox="0 0 56 56"><circle cx="28" cy="28" r="22" fill="none" stroke="#6cbd45" stroke-width="2.5" stroke-dasharray="30 5"/><text x="28" y="33" text-anchor="middle" font-family="Montserrat,sans-serif" font-size="14" fill="#2f2f2f">2</text></svg><div class="step-label current">Sorted &amp; Drained<br>Again</div></div>
<div class="abs step-divider" style="left:495px"></div>
<div class="abs step" style="left:499px"><svg width="56" height="56" viewBox="0 0 56 56"><circle cx="28" cy="28" r="22" fill="none" stroke="#6cbd45" stroke-width="2.5" stroke-dasharray="30 5"/><text x="28" y="33" text-anchor="middle" font-family="Montserrat,sans-serif" font-size="14" fill="#2f2f2f">3</text></svg><div class="step-label">Crushed into<br>Bricks</div></div>
<div class="abs step-divider" style="left:703px"></div>
<div class="abs step" style="left:704px"><svg width="56" height="56" viewBox="0 0 56 56"><circle cx="28" cy="28" r="22" fill="none" stroke="#6cbd45" stroke-width="2.5" stroke-dasharray="30 5"/><text x="28" y="33" text-anchor="middle" font-family="Montserrat,sans-serif" font-size="14" fill="#2f2f2f">4</text></svg><div class="step-label">Drained a 3rd<br>Time</div></div>
<div class="abs step-divider" style="left:910px"></div>
<div class="abs step" style="left:914px"><svg width="56" height="56" viewBox="0 0 56 56"><circle cx="28" cy="28" r="22" fill="none" stroke="#6cbd45" stroke-width="2.5" stroke-dasharray="30 5"/><text x="28" y="33" text-anchor="middle" font-family="Montserrat,sans-serif" font-size="14" fill="#2f2f2f">5</text></svg><div class="step-label">Ready for Metal<br>Recycling</div></div>

<!-- oil -->
<section class="abs oil" role="img" aria-label="Dark close-up of oil filter tops"></section>
<h2 class="abs center sec-title-light" style="top:2059px">What Happens to the Oil</h2>
<p class="abs center oil-text">All residual oil is <em>collected into our tanks</em> and then recycled. Currently we are processing<br><em>over 2,000 litres</em> of oil a month.</p>

<!-- gallery -->
<h2 class="abs center sec-title-blue" style="top:2295px">Photo Gallery</h2>
<div class="abs g-arrow" style="left:106px"><svg width="8" height="10" viewBox="0 0 8 10"><path d="M6 1L2 5l4 4" fill="none" stroke="#999" stroke-width="1.5"/></svg></div>
<div class="abs gallery-img g1" role="img" aria-label="Collection truck parked outside"></div>
<div class="abs gallery-img g2" role="img" aria-label="Filter processing machine"></div>
<div class="abs g2-overlay"><div class="g2-badge"><svg width="18" height="18" viewBox="0 0 18 18"><path d="M10 2h6v6M16 2l-6 6M8 16H2v-6M2 16l6-6" fill="none" stroke="#fff" stroke-width="2"/></svg></div>Filter Processing<br>Machine</div>
<div class="abs gallery-img g3" role="img" aria-label="Crushed filters on processing line"></div>
<div class="abs g-arrow" style="left:1064px"><svg width="8" height="10" viewBox="0 0 8 10"><path d="M2 1l4 4-4 4" fill="none" stroke="#999" stroke-width="1.5"/></svg></div>

<!-- contact -->
<section class="abs contact"></section>
<h2 class="abs center sec-title-light" style="top:2710px">Contact Us Today!</h2>
<div class="abs field" style="top:2774px;left:231px;width:258px;height:32px">Name</div>
<div class="abs field" style="top:2774px;left:504px;width:257px;height:32px">Email</div>
<div class="abs field" style="top:2774px;left:776px;width:193px;height:32px">Phone</div>
<div class="abs field" style="top:2824px;left:231px;width:738px;height:134px">Type your Message</div>
<div class="abs send"><svg width="18" height="18" viewBox="0 0 18 18"><path d="M1 8l16-7-6 16-2-7z" fill="#fff"/></svg></div>
<p class="abs center footer-addr"><svg width="10" height="12" viewBox="0 0 10 12" style="vertical-align:-1px;margin-right:6px"><path d="M5 0a4.5 4.5 0 0 1 4.5 4.5C9.5 8 5 12 5 12S.5 8 .5 4.5A4.5 4.5 0 0 1 5 0z" fill="#fff"/><circle cx="5" cy="4.5" r="1.6" fill="#2b4596"/></svg>Harlow Road, Linwood 4820, New Zealand</p>
<p class="abs center footer-call">Call Us: 06 555 0142 <span>&nbsp;| &nbsp;E.: support@brenmoorwaste.co.nz</span></p>
<div class="abs socials"><div class="social"></div><div class="social on"></div><div class="social"></div><div class="social"></div></div>
<svg class="abs" style="top:3028px;left:1087px" width="14" height="18" viewBox="0 0 14 18"><path d="M1 1h12v16l-6-5-6 5z" fill="none" stroke="rgba(255,255,255,.6)" stroke-width="1.5"/></svg>
<p class="abs center copyright">© 2017 Brenmoor Waste Solutions Ltd</p>

</body>
</html>
```